Brenmoor Group needs a business card

I would like the card to be simple but modern and elegant.
I like black and white.
or black and gold.
we are a private finance lender and also are involved in property and property developments.

please look at the business card photos i provided i would like B.G only one one side and all the other details on the other side use fonts that tie in with my theme.

Industry/Entity Type

Finance

Contact Information for Business Card

Brenmoor Group (B.G) Callum Brenmoor M: 0418396152 E: callumbren@quivomail.com

Font styles to use
Other font styles liked:
• Use fonts that would reflect our business

Colors
000000
ffffff

Requirements
Must have
• one side of details
• other side has either B.G or Brenmoor Group like in the photos provided

```html
<!DOCTYPE html>
<html lang="en">
<head>
<meta charset="utf-8">
<title>Brenmoor Group – Business Card</title>
<link rel="stylesheet" href="https://fonts.googleapis.com/css2?family=Oswald:wght@200;300&family=Roboto:ital,wght@0,300;1,300&display=swap">
<style>
  :root {
    --page: #ffffff;
    --card: #0b0b0b;
    --white: #ffffff;
    --muted: #6a6a6a;
    --gold-deep: #a8780f;
    --gold: #d9a91f;
    --gold-light: #f6dc72;
  }
  * { box-sizing: border-box; margin: 0; padding: 0; }
  html, body {
    width: 1190px;
    height: 1200px;
    overflow: hidden;
    background: var(--page);
  }
  .canvas {
    position: relative;
    width: 1190px;
    height: 1200px;
    display: flex;
    flex-direction: column;
    align-items: center;
    justify-content: center;
    gap: 66px;
  }
  .card {
    position: relative;
    width: 900px;
    height: 497px;
    background: var(--card);
    overflow: hidden;
  }

  /* Front: contact details */
  .contact {
    position: absolute;
    left: 0;
    right: 0;
    top: 196px;
    text-align: center;
    color: var(--white);
  }
  .contact__name {
    display: inline-block;
    font-family: "Oswald", "Arial Narrow", sans-serif;
    font-weight: 300;
    font-size: 44px;
    line-height: 1;
    letter-spacing: 0.56em;
    margin-right: -0.56em;
    text-transform: uppercase;
  }
  .contact__rule {
    width: 712px;
    height: 3px;
    margin: 10px auto 12px;
    background: linear-gradient(90deg, var(--gold-deep), var(--gold), var(--gold-light), var(--gold), var(--gold-deep));
  }
  .contact__line {
    font-family: "Roboto", "Helvetica", sans-serif;
    font-weight: 300;
    font-size: 22px;
    line-height: 27px;
  }
  .contact__line--email { font-style: italic; }

  /* Back: identity */
  .identity__rules {
    position: absolute;
    inset: 0;
    width: 900px;
    height: 497px;
  }
  .identity {
    position: absolute;
    left: 0;
    right: 0;
    top: 180px;
    display: flex;
    flex-direction: column;
    align-items: center;
  }
  .identity__mark {
    width: 66px;
    height: 66px;
    border-radius: 50%;
    background: var(--gold);
  }
  .identity__name {
    margin-top: 48px;
    color: var(--muted);
    font-family: "Oswald", "Arial Narrow", sans-serif;
    font-weight: 200;
    font-size: 24px;
    line-height: 1;
    letter-spacing: 0.3em;
    margin-right: -0.3em;
    text-transform: uppercase;
  }
</style>
</head>
<body>
<main class="canvas">

  <section class="card card--front" aria-label="Business card front">
    <div class="contact">
      <h1 class="contact__name">Callum Brenmoor</h1>
      <div class="contact__rule"></div>
      <p class="contact__line contact__line--phone">0418396152</p>
      <p class="contact__line contact__line--email">callumbren@quivomail.com</p>
    </div>
  </section>

  <section class="card card--back" aria-label="Business card back">
    <svg class="identity__rules" viewBox="0 0 900 497" aria-hidden="true">
      <defs>
        <linearGradient id="goldBar" x1="0" y1="0" x2="1" y2="0">
          <stop offset="0" stop-color="#a8780f"/>
          <stop offset="0.3" stop-color="#e9c248"/>
          <stop offset="0.55" stop-color="#f6dc72"/>
          <stop offset="0.8" stop-color="#c99619"/>
          <stop offset="1" stop-color="#e2b53a"/>
        </linearGradient>
      </defs>
      <rect x="96" y="80" width="713" height="8" fill="url(#goldBar)"/>
      <rect x="96" y="93" width="713" height="2.5" fill="url(#goldBar)"/>
      <rect x="96" y="402" width="713" height="8" fill="url(#goldBar)"/>
      <rect x="96" y="415" width="713" height="2.5" fill="url(#goldBar)"/>
    </svg>
    <div class="identity">
      <div class="identity__mark" aria-hidden="true"></div>
      <p class="identity__name">Brenmoor Group</p>
    </div>
  </section>

</main>
</body>
</html>
```